Real Estate Flyer (Brenton Property)

We need a color CMYK high resolution, print quality horizontal real estate property flyer designed in the sizes of 10" wide and 6.7425" tall and another one in 11" wide and 8.5" tall.
Ad should be professionally looking to U.S. standards. It should be sleek, modern yet classy.
We uploaded in Briefs logo files, agent photo, 2 photos of the property (Must use both) and a sample of a flyer for Vayle Morrow Luxury Residence. We like how the overlay atop the first photo in the Vayle Morrow flyer with the company logo in the overlay. We'd like to incorporate that with our logo, the background color of the overlay should match that of our logo. DON'T CHANGE LOGO COLORS. Only use two colors in ad (exact logo blue color and white). The text in the overlay must be "FOR SALE - Potential Income Producing Commercial Office Building". Other details that should be prominent underneath are "42 Brenton Dr., Schaumburg, IL 60174 - Asking Price: $650,000".
Add "Residential & Commercial" under our company logo in italic font.
Add in flyer: "Located seconds away from the Kettering Rd. & Palden Rd. Intersection"
Add in flyer:
- Completely vacant
- 10,000 sq. ft. building
- 55 Car Parking
- 1.38 acre lot
- Over 20 offices and 5 bathrooms.
- Lease out individual office spaces for great monthly cash flow
Put agent's photo and following details professionally displayed:
Dev Marlo
Managing Broker
847-555-0148
dev.marlo@qtnhomes-example.com
Add from Briefs fair housing logo and PLX logo near agent's information. Logos should be small but yet visible to understand text.
Add at bottom of the ad with separation near agent details:
Looking to Buy or Sell?
I’m your one-stop, full service licensed real estate broker.
I deal with all types of real estate properties: Homes, Condos, Townhomes, Multi-Unit Apartment Buildings and Commercial Spaces.
Let My Experience Guide You Through Every Step of the Process!
Fine print:
©2018 QTN Homes, Inc. All Rights Reserved.

```html
<!DOCTYPE html>
<html lang="en">
<head>
<meta charset="utf-8">
<title>Brenton Property – For Sale Flyer</title>
<link href="https://fonts.googleapis.com/css2?family=Lato:ital,wght@0,300;0,400;0,700;0,900;1,700&display=swap" rel="stylesheet">
<style>
  :root {
    --logo-blue: #0b4f9f;
    --overlay-blue: #34497e;
    --ink: #1d1d1f;
    --grey-text: #444;
    --rule: #9a9a9a;
    --white: #ffffff;
    --stage: #e4e4e6;
  }
  * { margin: 0; padding: 0; box-sizing: border-box; }
  html, body { width: 1200px; height: 1200px; overflow: hidden; background: var(--stage); font-family: "Lato", sans-serif; }
  .flyer { position: absolute; left: 0; top: 167px; width: 1200px; height: 866px; background: var(--white); overflow: hidden; }
  .abs { position: absolute; }

  .hero-photo { left: 0; top: 0; width: 1200px; height: 278px;
    background: linear-gradient(180deg, #c9ced4 0%, #d9b48c 35%, #e8dfcf 60%, #6f6a62 85%, #3f4248 100%); }

  .overlay { left: 0; top: 278px; width: 1200px; height: 173px; background: var(--overlay-blue); color: var(--white); }
  .for-sale { left: 0; width: 860px; top: 12px; text-align: center; font-weight: 900; font-size: 60px; letter-spacing: 13px; }
  .subline { left: 0; width: 860px; top: 87px; text-align: center; font-weight: 400; font-size: 26px; letter-spacing: 0.3px; }
  .address { left: 0; width: 860px; top: 124px; text-align: center; font-weight: 700; font-size: 26px; }
  .divider { left: 832px; top: 30px; width: 2px; height: 116px; background: var(--white); }
  .brand { left: 860px; width: 300px; top: 42px; text-align: center; }
  .brand-name { display: inline-flex; align-items: center; gap: 12px; font-weight: 900; font-size: 44px; letter-spacing: 1px; }
  .brand-name .mark { width: 20px; height: 20px; background: var(--white); }
  .brand-tag { left: 860px; width: 300px; top: 129px; text-align: center; font-style: italic; font-weight: 700; font-size: 19px; }

  .location { left: 0; width: 1200px; top: 459px; text-align: center; font-weight: 300; font-size: 31px; color: var(--ink); }

  .gallery-photo { top: 513px; height: 155px; border-radius: 12px; }
  .gallery-photo.one { left: 44px; width: 275px; background: linear-gradient(180deg, #c7cbd6 0%, #e4cfb4 45%, #6d6b63 70%, #2b2d31 100%); }
  .gallery-photo.two { left: 334px; width: 279px; background: linear-gradient(180deg, #b7bcc4 0%, #8a8172 40%, #3b3d42 60%, #2a2c30 100%); }

  .features { top: 700px; list-style: none; font-size: 16px; font-weight: 300; color: var(--ink); line-height: 20.5px; }
  .features.left { left: 66px; }
  .features.right { left: 306px; width: 290px; }
  .features li { position: relative; padding-left: 20px; }
  .features svg { position: absolute; left: 0; top: 5px; width: 14px; height: 11px; }

  .fine-print { left: 59px; top: 800px; font-size: 12px; color: var(--ink); }
  .footer-band { left: 0; top: 828px; width: 1200px; height: 38px; background: var(--logo-blue); }

  .pitch-title { left: 675px; top: 500px; font-weight: 900; font-size: 40px; color: var(--logo-blue); letter-spacing: -0.3px; }
  .pitch-copy { left: 677px; top: 557px; width: 490px; font-size: 13.6px; line-height: 19.5px; color: var(--ink); }
  .pitch-copy em { font-weight: 700; }
  .pitch-rule { left: 677px; top: 640px; width: 480px; height: 1px; background: var(--rule); }

  .agent { right: 213px; top: 650px; text-align: right; }
  .agent-name { font-weight: 900; font-size: 33px; color: var(--logo-blue); line-height: 38px; }
  .agent-role { font-weight: 300; font-size: 19px; color: var(--grey-text); line-height: 24px; }
  .agent-phone { font-weight: 700; font-size: 20px; color: var(--ink); line-height: 28px; display: flex; justify-content: flex-end; align-items: center; gap: 6px; }
  .agent-email { font-size: 19px; color: var(--ink); line-height: 24px; display: flex; justify-content: flex-end; align-items: center; gap: 6px; }
  .badges { right: 213px; top: 767px; display: flex; gap: 22px; align-items: center; }
  .badge-listing { width: 108px; height: 32px; border: 1.5px solid var(--grey-text); }
  .badge-housing { width: 40px; height: 34px; background: var(--ink); }
  .agent-photo { left: 1016px; top: 650px; width: 126px; height: 156px; border-radius: 10px; background: linear-gradient(180deg, #ececec 0%, #dcdcdc 55%, #2b2d33 75%, #1c1d22 100%); }
</style>
</head>
<body>
<main class="flyer">
  <div class="abs hero-photo" role="img" aria-label="Photo of the two-storey white office building with dormer windows at sunset, cars in the parking lot"></div>

  <section class="abs overlay">
    <h1 class="abs for-sale">FOR SALE</h1>
    <p class="abs subline">POTENTIAL INCOME PRODUCING COMMERCIAL OFFICE</p>
    <p class="abs address">42 Brenton Dr., Schaumburg, IL 60174 - Asking Price: $650,000</p>
    <div class="abs divider"></div>
    <div class="abs brand"><span class="brand-name"><span class="mark"></span>QTN Homes</span></div>
    <p class="abs brand-tag">Residential &amp; Commercial</p>
  </section>

  <p class="abs location">Located seconds away from the Kettering Rd. &amp; Palden Rd. Intersection</p>

  <div class="abs gallery-photo one" role="img" aria-label="Street view of the office building row along the parking lot"></div>
  <div class="abs gallery-photo two" role="img" aria-label="Parking lot with accessible parking spaces and trees"></div>

  <ul class="abs features left">
    <li><svg viewBox="0 0 14 11"><path d="M1 6 L5 10 L13 1" fill="none" stroke="var(--logo-blue)" stroke-width="2.4"/></svg>Completely vacant</li>
    <li><svg viewBox="0 0 14 11"><path d="M1 6 L5 10 L13 1" fill="none" stroke="var(--logo-blue)" stroke-width="2.4"/></svg>10,000 sq. ft. building</li>
    <li><svg viewBox="0 0 14 11"><path d="M1 6 L5 10 L13 1" fill="none" stroke="var(--logo-blue)" stroke-width="2.4"/></svg>55 Car Parking</li>
  </ul>
  <ul class="abs features right">
    <li><svg viewBox="0 0 14 11"><path d="M1 6 L5 10 L13 1" fill="none" stroke="var(--logo-blue)" stroke-width="2.4"/></svg>1.38 acre lot</li>
    <li><svg viewBox="0 0 14 11"><path d="M1 6 L5 10 L13 1" fill="none" stroke="var(--logo-blue)" stroke-width="2.4"/></svg>Over 20 offices and 5 bathrooms.</li>
    <li><svg viewBox="0 0 14 11"><path d="M1 6 L5 10 L13 1" fill="none" stroke="var(--logo-blue)" stroke-width="2.4"/></svg>Lease out individual office spaces for great monthly cash flow</li>
  </ul>

  <p class="abs fine-print">©2018 QTN Homes, Inc. All Rights Reserved.</p>

  <h2 class="abs pitch-title">Looking to Buy or Sell?</h2>
  <p class="abs pitch-copy">I’m your one-stop, full service licensed real estate broker.<br>
    I deal with all types of real estate properties: <em>Homes, Condos, Townhomes, Multi-Unit Apartment Buildings and Commercial Spaces.</em><br>
    Let My Experience Guide You Through Every Step of the Process!</p>
  <div class="abs pitch-rule"></div>

  <div class="abs agent">
    <p class="agent-name">Dev Marlo</p>
    <p class="agent-role">Managing Broker</p>
    <p class="agent-phone"><svg width="22" height="20" viewBox="0 0 22 20"><rect width="22" height="20" rx="4" fill="var(--logo-blue)"/><path d="M7 4 C5 6 6 10 9 13 C12 16 15 17 17 15 L15 12.5 L13 13.5 C11.5 12.5 9.5 10.5 8.5 9 L9.5 7 Z" fill="var(--white)"/></svg>847-555-0148</p>
    <p class="agent-email"><svg width="26" height="16" viewBox="0 0 26 16"><rect x="1" y="1" width="24" height="14" fill="none" stroke="var(--logo-blue)" stroke-width="1.5"/><path d="M1 1 L13 9 L25 1" fill="none" stroke="var(--logo-blue)" stroke-width="1.5"/></svg>dev.marlo@qtnhomes-example.com</p>
  </div>
  <div class="abs badges">
    <div class="badge-listing"></div>
    <div class="badge-housing"></div>
  </div>

  <div class="abs agent-photo" role="img" aria-label="Portrait photo of the managing broker in a dark suit and tie"></div>

  <div class="abs footer-band"></div>
</main>
</body>
</html>
```